Broschüre für Gleichstellungsstelle einer kommunalen Stadtverwaltung
Zielgruppe
Wir sind die Gleichstellungsstelle einer kommunalen Stadtverwaltung (Einwohner*innen ca. 74.500) und richten uns mit unserer Arbeit grundsätzlich an alle Menschen.
Wir wollen eine Broschüre zum Handlungsleitfaden für die geschlechtergerechte Sprache bei der Stadt erstellen. Dieser soll an die Beschäftigten als Unterstützung verteilt werden.
Aufgabenstellung
- Broschüre mit Wire-O-Bindung, Druckformat 14,8 cm x 14,8 cm, Endformat 15,0 x 15,0 cm
- Spiralbindung an der Kopfseite
- doppelseitiges Deckblatt und Rückseite
- 16 Seiten Inhalt, wobei lediglich die Vorderseiten Text enthalten
- Schriftart (optimal Avenir Next, alternativ Arial) und Farbschema laut Corporate Design
- Der Text ist vorgegeben, die Gestaltung ist im Rahmen des Corporate Designs frei
Es soll eine ansprechende Broschüre gestaltet werden, welche die Leser*innen zum Blättern einlädt. Das bedeutet, dass alle Seiten (Deckblatt, Inhaltsseiten und Rückseiten) bei der Gestaltung berücksichtigt werden müssen.
Am Ende soll neben den üblichen Dateien auch eine fertige Druckdatei (siehe Datenblatt) zur Verfügung gestellt werden. Dabei ist zu beachten, dass die Spiralbindung des fertigen Produkts an der Kopfseite sein soll.

```html
<!DOCTYPE html>
<html lang="de">
<head>
<meta charset="utf-8">
<title>Anrede in Briefen und E-Mails</title>
<link rel="stylesheet" href="https://fonts.googleapis.com/css2?family=Nunito+Sans:wght@400;600;700;800&display=swap">
<style>
  :root {
    --forest: #00504a;
    --accent-light: #a9c5bf;
    --teal-heading: #3f716a;
    --sage-box: #99b6b0;
    --text-grey: #5a5a5a;
    --white: #ffffff;
    --frame: #d6d6d6;
  }
  * { margin: 0; padding: 0; box-sizing: border-box; }
  html, body { width: 1200px; height: 1200px; overflow: hidden; background: var(--white); }
  body { font-family: "Nunito Sans", "Avenir Next", Arial, sans-serif; }

  .page {
    position: relative;
    width: 1200px;
    height: 1200px;
    background: var(--white);
    border: 1px solid var(--frame);
    overflow: hidden;
  }

  .intro-band {
    position: absolute;
    left: 0; top: 0;
    width: 1200px;
    height: 592px;
    background: var(--forest);
    color: var(--white);
    padding: 128px 80px 0 81px;
  }
  .intro-band h1 {
    font-size: 32px;
    font-weight: 800;
    letter-spacing: 0.2px;
    line-height: 40px;
  }
  .intro-band p {
    font-size: 26px;
    line-height: 32.5px;
    font-weight: 400;
  }
  .intro-band .lead { margin-top: 1px; }
  .intro-band .lead strong { color: var(--accent-light); font-weight: 700; }
  .intro-band .detail { margin-top: 32px; }
  .intro-band .example-cue { font-size: 27px; margin-top: 2px; }

  .comparison {
    position: absolute;
    top: 648px;
    left: 81px;
    width: 1040px;
    display: flex;
  }
  .comparison .column { width: 520px; }
  .comparison h2 {
    font-size: 32px;
    font-weight: 700;
    color: var(--teal-heading);
    line-height: 40px;
  }
  .comparison ul { list-style: none; color: var(--text-grey); }
  .column--avoid ul li { font-size: 26px; line-height: 39px; }
  .column--prefer ul li { font-size: 27px; line-height: 42px; }
  .column--prefer h2 { margin-bottom: 2px; }

  .greeting-note {
    position: absolute;
    left: 81px;
    top: 842px;
    font-size: 26px;
    color: var(--text-grey);
    line-height: 34px;
  }
  .greeting-box {
    position: absolute;
    left: 336px;
    top: 896px;
    width: 479px;
    height: 75px;
    background: var(--sage-box);
    color: var(--white);
    font-size: 35px;
    font-weight: 700;
    display: flex;
    align-items: center;
    justify-content: center;
  }
  .greeting-close {
    position: absolute;
    left: 81px;
    top: 996px;
    font-size: 26px;
    color: var(--text-grey);
    line-height: 34px;
  }
</style>
</head>
<body>
  <main class="page">
    <section class="intro-band">
      <h1>ANREDE IN BRIEFEN UND E-MAILS</h1>
      <p class="lead">Zur Anrede in allgemeinen Briefen oder E-Mails sollte auf <strong>neutrale<br>Personenbezeichnungen</strong> oder auf das Gendersternchen zurück-<br>gegriffen werden.</p>
      <p class="detail">Falls einzelne Personen direkt angesprochen werden sollen, kann durch<br>eine persönliche Ansprache, also der Nennung des Vor- und Nachnamen<br>(statt Frau/Herr) geschlechtersensibel formuliert werden. Auch auf<br>Anwesenheitslisten ist die Bezeichnung Frau/Herr in der Regel überflüssig.</p>
      <p class="example-cue">Zum Beispiel:</p>
    </section>

    <section class="comparison">
      <div class="column column--avoid">
        <h2>statt:</h2>
        <ul>
          <li>Frau Maier</li>
          <li>Herr und Frau Meier</li>
          <li>Herr und Frau Maier</li>
        </ul>
      </div>
      <div class="column column--prefer">
        <h2>besser:</h2>
        <ul>
          <li>Petra Maier</li>
          <li>Petra und Hans Maier</li>
          <li>Familie Maier</li>
        </ul>
      </div>
    </section>

    <p class="greeting-note">Als Grußformel bieten sich hier je nach Kontext</p>
    <div class="greeting-box">„Hallo“, „Guten Tag“</div>
    <p class="greeting-close">oder ähnliches an.</p>
  </main>
</body>
</html>
```